Kestrel Mobile App Design Concept

Design concept, including wireframe and design comps for a basketball themed Kestrel Mobile app.
Need example of a panorama page with 3 or 4 panels to include game schedule, news and a menu.
Example of a detail page showing game info or player info.
Note this quote is for a design concept.The chosen designer will be asked to work with our development team to build the full app. Familiarity with Balsamiq an advantage
Reason: Designs still in process from interested parties.
- 1. Must follow Kestrel Mobile guide lines
2. Must not look like an zelpad app
3. Dark theme and background

```html
<!DOCTYPE html>
<html lang="en">
<head>
<meta charset="utf-8">
<title>Courtside Live – Kestrel Mobile app concept</title>
<link rel="stylesheet" href="https://fonts.googleapis.com/css2?family=Open+Sans:wght@300;400;600;700;800&display=swap">
<style>
:root{
  --stage:#3a3546;
  --screen:#070709;
  --screen-glow:#1d1c26;
  --appbar:#262626;
  --text:#ffffff;
  --muted:#a8a8a8;
  --faint:#3c3c3c;
  --green:#1ee61e;
  --yellow:#f7c51b;
  --blue:#0b6fe6;
  --red:#f25252;
  --cyan:#0aaee8;
  --magenta:#c20fb6;
  --stat-label:#19a3e6;
  --stat-value:#3a3a3a;
}
*{margin:0;padding:0;box-sizing:border-box}
html,body{width:1200px;height:1108px;overflow:hidden;background:var(--stage);font-family:"Open Sans",sans-serif;color:var(--text)}
.canvas{display:flex;justify-content:center;gap:36px;padding-top:214px}
.screen{position:relative;width:350px;height:640px;overflow:hidden;
  background:radial-gradient(ellipse at 70% 40%,var(--screen-glow),var(--screen) 70%);box-shadow:0 30px 60px rgba(0,0,0,.45)}
.brand{font-family:"Open Sans",sans-serif;font-weight:700;font-size:52px;line-height:1.1;white-space:nowrap;margin:22px 0 0 16px}
.page-title{font-weight:300;font-size:54px;line-height:1;margin:2px 0 0 18px;white-space:nowrap}
.appbar{position:absolute;left:0;right:0;bottom:0;height:62px;background:var(--appbar);display:flex;justify-content:center;gap:26px;padding-top:10px}
.appbar .more{position:absolute;right:14px;top:2px;font-size:20px;letter-spacing:2px;line-height:1}
.round-btn{width:34px;height:34px}
/* home tiles */
.tiles{display:grid;grid-template-columns:150px 150px;gap:8px;margin:16px 0 0 18px}
.tile{height:126px;position:relative;display:flex;align-items:center;justify-content:center}
.tile .label{position:absolute;left:8px;bottom:6px;font-size:14px}
.tile.news{background:var(--green)}.tile.scores{background:var(--yellow)}
.tile.schedule{background:var(--blue)}.tile.standings{background:var(--red)}
.tile.teams{background:var(--cyan)}.tile.players{background:var(--magenta)}
.scoreline{font-weight:800;font-size:32px}
/* news */
.news-list{list-style:none;margin:14px 0 0 18px}
.news-item{display:flex;gap:10px;margin-bottom:12px}
.thumb{width:70px;height:58px;flex:none}
.headline{font-weight:800;font-size:17px;line-height:1.1;white-space:nowrap}
.summary{font-size:12px;color:var(--muted);line-height:1.25;max-width:240px}
/* player */
.eyebrow{font-weight:700;font-size:13px;margin:22px 0 0 18px}
.pivot{display:flex;gap:14px;margin-left:16px;font-weight:300;font-size:54px;line-height:1}
.pivot .inactive{color:var(--faint)}
.profile{display:flex;gap:12px;margin:14px 0 0 18px}
.portrait{width:150px;height:118px;background:linear-gradient(160deg,#f2efe9,#b8896a 60%,#5a3b2a)}
.player-name{font-weight:800;font-size:34px;line-height:.95;text-transform:uppercase}
.player-team{font-size:13px;color:var(--muted);text-transform:uppercase;margin-top:4px}
.section-title{font-weight:700;font-size:13px;margin:14px 0 4px 18px}
.stats{display:flex;gap:8px;margin-left:18px}
.stat{width:98px}
.stat dt{background:var(--stat-label);font-weight:800;font-size:15px;padding:1px 8px}
.stat dd{background:var(--stat-value);font-weight:300;font-size:26px;padding:2px 8px}
.bio{margin:14px 18px 0;font-size:13px;line-height:1.3}
.bio strong{display:block;font-weight:800;font-size:14px}
</style>
</head>
<body>
<main class="canvas">

  <!-- home panorama -->
  <section class="screen home">
    <h1 class="brand">Courtside</h1>
    <h2 class="page-title">home</h2>
    <div class="tiles">
      <a class="tile news"><svg width="56" height="42" viewBox="0 0 56 42" fill="none" stroke="#fff" stroke-width="4"><rect x="2" y="2" width="52" height="38"/><path d="M10 12h36M10 21h16M10 30h16M32 21h14M32 30h14"/></svg><span class="label">News</span></a>
      <a class="tile scores"><span class="scoreline">1:1</span><span class="label">Scores</span></a>
      <a class="tile standings"><svg width="50" height="50" viewBox="0 0 50 50" fill="#fff"><rect x="4" y="30" width="10" height="18"/><rect x="20" y="18" width="10" height="30"/><rect x="36" y="4" width="10" height="44"/></svg><span class="label">Standings</span></a>
      <a class="tile schedule"><svg width="58" height="58" viewBox="0 0 58 58" fill="none" stroke="#fff" stroke-width="4"><circle cx="29" cy="29" r="26"/><rect x="17" y="19" width="24" height="20"/><text x="29" y="34" fill="#fff" stroke="none" font-size="11" font-weight="700" text-anchor="middle" font-family="Open Sans,sans-serif">25</text></svg><span class="label">Schedule</span></a>
      <a class="tile players"><svg width="58" height="58" viewBox="0 0 58 58" fill="none" stroke="#fff" stroke-width="4"><circle cx="29" cy="29" r="26"/><circle cx="29" cy="23" r="8" fill="#fff"/><path d="M15 44c2-9 26-9 28 0z" fill="#fff"/></svg><span class="label">Players</span></a>
      <a class="tile teams"><svg width="58" height="58" viewBox="0 0 58 58" fill="none" stroke="#fff" stroke-width="4"><circle cx="29" cy="29" r="26"/><circle cx="24" cy="24" r="6" fill="#fff"/><circle cx="35" cy="24" r="6" fill="#fff"/><path d="M13 42c2-8 20-8 22 0zM26 42c2-8 18-8 20 0z" fill="#fff"/></svg><span class="label">Teams</span></a>
    </div>
    <nav class="appbar">
      <svg class="round-btn" viewBox="0 0 34 34" fill="none" stroke="#fff" stroke-width="2.5"><circle cx="17" cy="17" r="15"/><circle cx="18" cy="15" r="5"/><path d="M14 19l-4 4"/></svg>
      <svg class="round-btn" viewBox="0 0 34 34" fill="none" stroke="#fff" stroke-width="2.5"><circle cx="17" cy="17" r="15"/><path d="M10 16a7 7 0 0 1 13-3M24 18a7 7 0 0 1-13 3"/><path d="M23 9v5h-5M11 25v-5h5"/></svg>
      <span class="more">•••</span>
    </nav>
  </section>

  <!-- news panel -->
  <section class="screen news">
    <h1 class="brand">Live</h1>
    <h2 class="page-title">news</h2>
    <ul class="news-list">
      <li class="news-item"><div class="thumb" role="img" aria-label="Coach headshot" style="background:linear-gradient(#d9d4ce,#8a7d74)"></div><div><p class="headline">Dale Harwick</p><p class="summary">RIVERTON — Riverton Hawks coach<br>held under influence of alcohol</p></div></li>
      <li class="news-item"><div class="thumb" role="img" aria-label="Game action photo" style="background:linear-gradient(#6c5a4a,#2d3f6b)"></div><div><p class="headline">Is Troy Mendel</p><p class="summary">First Alvin Reese, now Mendel<br>week after ...</p></div></li>
      <li class="news-item"><div class="thumb" role="img" aria-label="Team badge image" style="background:linear-gradient(#f2f2f2,#c9d3e8)"></div><div><p class="headline">Coasters sign Anton</p><p class="summary">The Bayside Coasters signed<br>forward Anton Jarrell today</p></div></li>
      <li class="news-item"><div class="thumb" role="img" aria-label="Player portrait photo" style="background:linear-gradient(#e7e2dc,#4a3327)"></div><div><p class="headline">Ian Jensen to</p><p class="summary">Free-agent forward Ian Jensen<br>Eastbay Chargers bound</p></div></li>
      <li class="news-item"><div class="thumb" role="img" aria-label="Player on court photo" style="background:linear-gradient(#3c3431,#a98e7c)"></div><div><p class="headline">DA won't file against<br>Pemberton</p></div></li>
      <li class="news-item"><div class="thumb" role="img" aria-label="Game action photo" style="background:linear-gradient(#2f3e73,#c9bcb0)"></div><div><p class="headline">The Final Countdown</p><p class="summary">Jonah Parker found Joel Andrews<br>for a 5-yard TD</p></div></li>
    </ul>
    <nav class="appbar">
      <svg class="round-btn" viewBox="0 0 34 34" fill="none" stroke="#fff" stroke-width="2.5"><circle cx="17" cy="17" r="15"/><circle cx="18" cy="15" r="5"/><path d="M14 19l-4 4"/></svg>
      <svg class="round-btn" viewBox="0 0 34 34" fill="none" stroke="#fff" stroke-width="2.5"><circle cx="17" cy="17" r="15"/><path d="M10 16a7 7 0 0 1 13-3M24 18a7 7 0 0 1-13 3"/><path d="M23 9v5h-5M11 25v-5h5"/></svg>
      <span class="more">•••</span>
    </nav>
  </section>

  <!-- player detail -->
  <section class="screen player">
    <p class="eyebrow">PLAYERS</p>
    <div class="pivot"><span>info</span><span class="inactive">profile</span></div>
    <div class="profile">
      <div class="portrait" role="img" aria-label="Player portrait photo"></div>
      <div><p class="player-name">Marcus<br>Vale</p><p class="player-team">Harbor City</p></div>
    </div>
    <p class="section-title">2012 - 2013 season</p>
    <dl class="stats">
      <div class="stat"><dt>PPG</dt><dd>27.3</dd></div>
      <div class="stat"><dt>APG</dt><dd>6.0</dd></div>
      <div class="stat"><dt>RPG</dt><dd>5.3</dd></div>
    </dl>
    <p class="section-title">Career</p>
    <dl class="stats">
      <div class="stat"><dt>PPG</dt><dd>25.5</dd></div>
      <div class="stat"><dt>APG</dt><dd>4.8</dd></div>
      <div class="stat"><dt>RPG</dt><dd>5.3</dd></div>
    </dl>
    <p class="bio"><strong>Bio</strong>Marcus Vale is a shooting guard who has played for the Harbor City Comets since</p>
    <nav class="appbar">
      <svg class="round-btn" viewBox="0 0 34 34" fill="none" stroke="#fff" stroke-width="2.5"><circle cx="17" cy="17" r="15"/><circle cx="18" cy="15" r="5"/><path d="M14 19l-4 4"/></svg>
    </nav>
  </section>

</main>
</body>
</html>
```